依頼詳細
コロナ化でのお客様の配慮等も含めました感謝を込めた内容に仕上げていただきますとありがたいです。
記載項目
BAR KVO
〒071-0413
北海道札幌市中央区北3条東9丁目 ミドリ荘月光棟 4階
営業時間 21:00~5:00 TEL011-522-0978
希望イメージ
シンプル 複雑
単色 カラフル
暗い 明るい
日常 高級
遊び心 厳粛
未来的 伝統的
女性的 男性的
希望する色
設定なし
納品ファイル
• 高解像度JPG (.jpg)
• イラストレーター形式 (.ai)
• フォトショップ形式 (.psd)
補足説明
6周年の案内文面も希望します。
周年の期日を記載できるスペース内容を追加お願いします。
申し訳ありませんが、この度コロナ感染拡大につき周年イベント日時を伸ばすことにしましたので締め切り日程も延長いたしました、引き続きよろしくお願いいたします。
依頼金額を12100円に変更して、延長しました。
新型コロナウイルス感染症対策の、まん延防止等重点措置の、時短営業により周年期日を延長する事になりました。
依頼金額を13500円に変更して、延長しました。

この時期に合うデザインでした。

この度は、素敵なデザイン案作成誠にありがとうございました。

文面等修正依頼したいので後日再度ご連絡いたしますのでよろしくお願いいたします。

```html
<!DOCTYPE html>
<html lang="ja">
<head>
<meta charset="utf-8">
<title>BAR KVO 6周年のご挨拶</title>
<link rel="stylesheet" href="https://fonts.googleapis.com/css2?family=Shippori+Mincho:wght@500;700;800&family=Noto+Serif+JP:wght@400;600&display=swap">
<style>
  :root {
    --paper: #ffffff;
    --blush: #f6e9ea;
    --crimson: #8c1c2c;
    --crimson-deep: #6a0f1c;
    --wine: #7a1626;
    --rose: #c99aa2;
    --ink: #2b1a1c;
    --gold: #c9a24a;
    --cream: #f3e6d6;
  }
  * { margin: 0; padding: 0; box-sizing: border-box; }
  html, body { width: 813px; height: 1200px; overflow: hidden; background: var(--paper); }
  .card {
    position: relative;
    width: 813px; height: 1200px;
    background: linear-gradient(180deg, var(--paper) 0%, var(--paper) 62%, var(--blush) 72%, #e8c9cd 80%, var(--crimson) 88%, var(--crimson-deep) 100%);
    font-family: "Noto Serif JP", serif;
    color: var(--ink);
    overflow: hidden;
  }
  .header-rule { position: absolute; left: 0; top: 0; width: 813px; height: 180px; }
  .title {
    position: absolute; top: 80px; left: 0; width: 100%;
    text-align: center;
    font-family: "Shippori Mincho", serif;
    font-weight: 800; font-size: 56px; letter-spacing: 2px;
    color: var(--wine);
  }
  .message {
    position: absolute; top: 190px; left: 0; width: 100%;
    text-align: center; font-size: 16px; line-height: 28px;
    letter-spacing: 1px;
  }
  .message p + p { margin-top: 22px; }
  .hero {
    position: absolute; left: 150px; top: 460px; width: 520px; height: 620px;
    border-radius: 48% 48% 20px 20px;
    background:
      radial-gradient(ellipse at 50% 40%, rgba(230,190,100,0.75) 0%, rgba(201,162,74,0.35) 25%, transparent 45%),
      radial-gradient(ellipse at 50% 55%, #b3283a 0%, #8c1c2c 55%, rgba(106,15,28,0.0) 100%);
  }
  .date-box {
    position: absolute; left: 632px; top: 870px; width: 168px; height: 120px;
    background: var(--cream);
    border: 2px solid var(--gold);
    display: flex; align-items: center; justify-content: center;
    text-align: center;
    font-family: "Shippori Mincho", serif; font-weight: 700;
    font-size: 20px; line-height: 30px; color: var(--wine);
  }
  .footer {
    position: absolute; left: 0; bottom: 0; width: 100%; height: 112px;
    display: flex; align-items: center; gap: 24px; padding: 0 28px;
    color: var(--cream);
  }
  .brand {
    display: flex; align-items: center; gap: 8px;
    flex: none;
    font-family: "Shippori Mincho", serif; font-weight: 700; font-size: 19px;
    color: var(--cream);
    white-space: nowrap;
  }
  .brand-dot { width: 14px; height: 14px; border-radius: 50%; background: var(--cream); }
  .contact { font-size: 15px; line-height: 26px; letter-spacing: 0.5px; white-space: nowrap; }
</style>
</head>
<body>
<main class="card">
  <svg class="header-rule" viewBox="0 0 813 180" aria-hidden="true">
    <path d="M40 60 Q406 20 773 60" fill="none" stroke="var(--crimson)" stroke-width="3"/>
    <path d="M40 70 Q406 30 773 70" fill="none" stroke="var(--rose)" stroke-width="1.5"/>
    <line x1="60" y1="166" x2="753" y2="166" stroke="var(--rose)" stroke-width="1"/>
  </svg>

  <h1 class="title">おかげさまで6周年!!</h1>

  <section class="message">
    <p>弊店は2021年〇月〇日をもちまして、<br>開店6周年を迎えることとなりました。<br>これもひとえに皆様のご支援の賜物と心より感謝しております。</p>
    <p>このコロナ禍の中、飲食店には厳しい日々が続きますが、<br>皆様に安心してお食事を楽しんでいただけます様に、<br>体調管理・感染対策も今まで以上に徹底してまいります。<br>スタッフ一同、心をこめておもてなしさせて頂きますので、<br>今後とも よろしくご愛顧の程お願い申し上げます。</p>
  </section>

  <div class="hero" role="img" aria-label="赤いベルベットの椅子に金色の6thの数字とリボンが飾られたイラスト"></div>

  <div class="date-box">周年の<br>期日スペース</div>

  <footer class="footer">
    <div class="brand"><span class="brand-dot"></span>BAR KVO</div>
    <div class="contact">
      〒071-0413 北海道札幌市中央区北3条東9丁目 ミドリ荘月光棟 4階<br>
      営業時間 21:00~5:00　TEL011-739-4152
    </div>
  </footer>
</main>
</body>
</html>
```